Need Business Card for our Indian Grocery Store

Industry/Entity Type

Grocery Store

Contact Information for Business Card

Manoj Baweja
Director

Store Locations:

Glenbrook
482 Elm Parade
P: 03 9172 5843

Ashvale
613 Carlow Road
P: 03 9238 6014

email: kvtmarts@mailnest.example

Requirements
Must have
• Our logo Colours

```html
<!DOCTYPE html>
<html lang="en">
<head>
<meta charset="utf-8">
<title>KVT Marts Business Card</title>
<link href="https://fonts.googleapis.com/css2?family=Lato:wght@400;700;900&display=swap" rel="stylesheet">
<style>
  :root {
    --brand-red: #e21f26;
    --paper: #ffffff;
    --backdrop: #2b2b2d;
    --text-font: "Lato", Arial, sans-serif;
  }
  * { box-sizing: border-box; margin: 0; padding: 0; }
  html, body {
    width: 1200px;
    height: 1189px;
    overflow: hidden;
    background: var(--backdrop);
    font-family: var(--text-font);
  }
  .canvas {
    position: relative;
    width: 1200px;
    height: 1189px;
  }
  .card {
    position: absolute;
    left: 170px;
    width: 860px;
    height: 491px;
    border-radius: 34px;
    overflow: hidden;
  }
  .card--front {
    top: 60px;
    background: var(--brand-red);
    display: flex;
    align-items: center;
    justify-content: center;
  }
  .card--back {
    top: 638px;
    background: var(--paper);
  }
  .brand {
    display: flex;
    flex-direction: column;
    align-items: center;
  }
  .brand__name {
    font-weight: 900;
    font-size: 64px;
    letter-spacing: 4px;
    line-height: 1;
  }
  .brand__tagline {
    margin-top: 14px;
    font-size: 20px;
    letter-spacing: 1px;
    display: flex;
    align-items: center;
    gap: 12px;
  }
  .brand__tagline::before,
  .brand__tagline::after {
    content: "";
    width: 28px;
    height: 2px;
    background: currentColor;
  }
  .card--front .brand { color: var(--paper); }
  .card--back .brand {
    position: absolute;
    top: 58px;
    left: 0;
    right: 0;
    color: var(--brand-red);
  }
  .contact-band {
    position: absolute;
    left: 0;
    right: 0;
    top: 212px;
    height: 178px;
    background: var(--brand-red);
    color: var(--paper);
    text-align: center;
  }
  .person { margin-top: 20px; }
  .person__name {
    font-weight: 700;
    font-size: 26px;
    line-height: 1.1;
  }
  .person__title { font-size: 19px; }
  .locations {
    display: flex;
    justify-content: center;
    margin-top: 18px;
  }
  .location {
    padding: 0 26px;
    font-size: 19px;
    line-height: 1.3;
  }
  .location--left { text-align: right; }
  .location--right {
    text-align: left;
    border-left: 2px solid var(--paper);
  }
  .location__suburb { font-weight: 700; }
  .location__phone strong { font-weight: 700; }
  .email {
    position: absolute;
    left: 0;
    right: 0;
    top: 414px;
    text-align: center;
    color: var(--brand-red);
    font-size: 24px;
    letter-spacing: 2px;
  }
</style>
</head>
<body>
<main class="canvas">
  <section class="card card--front" aria-label="Card front">
    <div class="brand">
      <div class="brand__name">KVT MARTS</div>
      <div class="brand__tagline">Fresh Pantry Since 2011</div>
    </div>
  </section>

  <section class="card card--back" aria-label="Card back">
    <div class="brand">
      <div class="brand__name">KVT MARTS</div>
      <div class="brand__tagline">Fresh Pantry Since 2011</div>
    </div>

    <div class="contact-band">
      <div class="person">
        <div class="person__name">Manoj Baweja</div>
        <div class="person__title">Director</div>
      </div>
      <div class="locations">
        <div class="location location--left">
          <div class="location__suburb">Glenbrook</div>
          <div class="location__phone">482 Elm Parade | <strong>P:</strong> 03 9172 5843</div>
        </div>
        <div class="location location--right">
          <div class="location__suburb">Ashvale</div>
          <div class="location__phone">613 Carlow Road | <strong>P:</strong> 03 9238 6014</div>
        </div>
      </div>
    </div>

    <div class="email">kvtmarts@mailnest.example</div>
  </section>
</main>
</body>
</html>
```